Meridian Span Partners needs a business card design

Business card should represent civil engineering infrastructure projects such as roads, bridges, tunnels, rail, rail, pipelines, structures and resource infrastructure

Industry/Entity Type

Business

```html
<!DOCTYPE html>
<html lang="en">
<head>
<meta charset="utf-8">
<title>Meridian Span Partners – Business Card</title>
<link rel="stylesheet" href="https://fonts.googleapis.com/css2?family=Questrial&display=swap">
<style>
  :root {
    --sand: #e9e59b;
    --lagoon: #35bfd6;
    --ink: #1e1a14;
    --paper: #ffffff;
    --brass-light: #c9a86a;
    --brass-dark: #4a3424;
  }
  * { margin: 0; padding: 0; box-sizing: border-box; }
  html, body {
    width: 1200px;
    height: 347px;
    overflow: hidden;
    background: var(--paper);
  }
  body {
    position: relative;
    font-family: "Questrial", "Helvetica Neue", Arial, sans-serif;
    color: var(--ink);
  }
  .card {
    position: absolute;
    top: 0;
    height: 347px;
    background: var(--sand);
    overflow: hidden;
  }
  .card--front { left: 0; width: 580px; }
  .card--back { left: 621px; width: 579px; }

  .contact-band {
    position: absolute;
    left: 0;
    top: 194px;
    width: 100%;
    height: 153px;
    background: var(--lagoon);
  }

  .brand-name {
    position: absolute;
    font-size: 26px;
    letter-spacing: 1px;
    color: var(--ink);
  }
  .instrument-art {
    position: absolute;
    display: block;
  }

  .card--front .brand-name { left: 98px; top: 44px; }
  .card--front .instrument-art { left: 86px; top: 80px; width: 104px; height: 92px; }

  .holder-name {
    position: absolute;
    left: 236px;
    top: 106px;
    font-size: 28px;
    letter-spacing: 0.3px;
  }

  .contact-list {
    position: absolute;
    left: 84px;
    top: 236px;
    list-style: none;
    font-size: 16px;
    line-height: 21px;
    color: #111;
  }

  .card--back .brand-name { left: 147px; top: 92px; }
  .card--back .instrument-art { left: 134px; top: 136px; width: 108px; height: 92px; }

  .firm-words {
    position: absolute;
    font-size: 16px;
    line-height: 1;
  }
  .firm-words span { position: absolute; white-space: nowrap; }
  .firm-words .w1 { left: 302px; top: 138px; }
  .firm-words .w2 { left: 356px; top: 170px; }
  .firm-words .w3 { left: 317px; top: 201px; }
</style>
</head>
<body>

  <section class="card card--front">
    <div class="brand-name">MSP</div>
    <svg class="instrument-art" viewBox="0 0 104 92" role="img" aria-label="Illustration of a brass navigational sextant">
      <defs>
        <radialGradient id="brassFront" cx="50%" cy="50%" r="60%">
          <stop offset="0%" stop-color="var(--brass-light)"/>
          <stop offset="100%" stop-color="var(--brass-dark)"/>
        </radialGradient>
      </defs>
      <rect width="104" height="92" rx="6" fill="url(#brassFront)"/>
    </svg>
    <h1 class="holder-name" style="font-weight:400">Thomas Alan Reeve</h1>

    <div class="contact-band">
    </div>
    <ul class="contact-list">
      <li>thomas.reeve@meridianspanpartners.com.au</li>
      <li>thomas.alan.reeve@mailbox.net</li>
      <li>+61400123456</li>
    </ul>
  </section>

  <section class="card card--back">
    <div class="brand-name">MSP</div>
    <svg class="instrument-art" viewBox="0 0 108 92" role="img" aria-label="Illustration of a brass navigational sextant">
      <defs>
        <radialGradient id="brassBack" cx="50%" cy="50%" r="60%">
          <stop offset="0%" stop-color="var(--brass-light)"/>
          <stop offset="100%" stop-color="var(--brass-dark)"/>
        </radialGradient>
      </defs>
      <rect width="108" height="92" rx="6" fill="url(#brassBack)"/>
    </svg>
    <div class="firm-words">
      <span class="w1">meridian</span>
      <span class="w2">span</span>
      <span class="w3">partners</span>
    </div>
  </section>

</body>
</html>
```